Cover design brief for the “Lanterns along the river” collection

This collection aims to publish articles by several authors who are practitioners specializing in sociocracy, a participatory mode of governance that is highly innovative, and even quite subversive of the autocratic way in which companies and public institutions operate. However, this method has been widely and increasingly implemented since its initial development in the Netherlands in the 1970s and 80s. It is currently of particular interest to non-profit and cooperative organizations, citizen projects and intentional communities, as well as IT work teams (due to its proximity to the spirit of Agile methods).
The content is intellectually demanding. It won't be a matter of popularization for promotional purposes, but rather of subjects for reflection or in-depth analysis of practices, and feedback from field experience. Nor is it an academic journal.
The language used for these publications is French.
The target audience is French-speaking Europe and Canada.

Target Market(s)

The collection is aimed both at other practitioners of this method who want to develop their knowledge, and at people interested in the subjects of collective intelligence, cooperation and organization, in response to social, ecological and/or political concerns.

Industry/Entity Type

Training and consultancy

Font styles to use
Sans Serif

Requirements
Must have
• The name of the collection: Lanterns along the river - Weaving a quieter commons Each volume will mention the name of the collection as well as the theme of the volume. First one: Volume 1 - Mapping hidden currents within shared endeavours. Selection criteria: - A singular, recurring visual identity for the volumes in the collection, highlighting its theme. - Appeal to potential readers; arouse curiosity. - Good readability of the text (title and subtitle, authors; presentation on back cover). - Simplicity of design variation for the cover of subsequent volumes (changing only the text). - Reasonable price in relation to a hoped-for circulation of between 100 and 300 copies per volume (the theme is linked to a niche that is still fairly narrow in the French-speaking world).
Nice to have
• Suggested graphic design directions If you have another direction to suggest with convincing arguments, we're open to your proposal. - The name of the collection, and in particular "Lanterns along the river", will be visible at first glance. - The overall visual impression is one of movement and dynamism. - The style will be based on illustration work, such as sketchnotes. - The tone is playful and humorous. For example, it may mirror back to the potential reader the cultural clichés and social norms about power that make the theme "lanterns along the river" a challenge to his or her imagination. As stated in the preface to Volume 1: "Most people are used to social environments where the choice is limited to suffering or fighting against powers that seek in a multitude of ways to put us at their service..."

```html
<!DOCTYPE html>
<html lang="en">
<head>
<meta charset="utf-8">
<title>Lanterns along the river – Volume 1</title>
<link href="https://fonts.googleapis.com/css2?family=Playfair+Display:wght@700;900&family=Raleway:wght@400;500&display=swap" rel="stylesheet">
<style>
  :root{
    --backdrop:#333132;
    --paper:#ffffff;
    --ink:#111111;
    --red-light:#d42a42;
    --red-dark:#9b1b2c;
    --lime:#d4e80f;
    --lime-soft:#eef58a;
  }
  *{margin:0;padding:0;box-sizing:border-box}
  html,body{width:1200px;height:675px;overflow:hidden;background:var(--backdrop)}
  .stage{position:relative;width:1200px;height:675px;background:var(--backdrop)}
  .cover{position:absolute;left:365px;top:0;width:469px;height:675px;background:var(--paper);overflow:hidden}
  .centered{position:absolute;left:0;width:100%;text-align:center;line-height:1}

  .volume-line{top:18px;font-family:"Raleway",sans-serif;font-size:12.5px;letter-spacing:2.6px;color:var(--ink);line-height:17px;font-weight:500}
  .volume-line .volume-tag{font-family:"Playfair Display",serif;font-weight:700;font-size:14px;letter-spacing:2px}

  .title-red{font-family:"Playfair Display",serif;font-weight:900;
    background:linear-gradient(180deg,var(--red-light) 0%,var(--red-dark) 100%);
    -webkit-background-clip:text;background-clip:text;color:transparent}
  .title-lanterns{top:128px;font-size:78px;letter-spacing:-1px}
  .title-river{top:254px;font-size:96px;letter-spacing:1px}

  .ruled{position:absolute;left:0;width:100%;display:flex;align-items:center;justify-content:center;gap:10px}
  .ruled .rule{width:60px;height:4px;background:var(--ink);clip-path:polygon(0 50%,100% 0,100% 100%)}
  .ruled .rule.right{clip-path:polygon(0 0,100% 50%,0 100%)}
  .ruled .word{font-family:"Playfair Display",serif;font-weight:700;font-size:38px;color:var(--ink);line-height:1}
  .title-along{top:214px}

  .concept-art{position:absolute;left:57px;top:356px;width:306px;height:160px;
    background:linear-gradient(120deg,var(--lime) 0%,var(--lime-soft) 100%)}

  .subtitle{top:534px;font-family:"Raleway",sans-serif;font-weight:400;font-size:22px;letter-spacing:5px;line-height:26px;color:var(--ink)}
  .authors{top:605px;font-family:"Playfair Display",serif;font-weight:900;font-size:27px;letter-spacing:4px;line-height:27px;color:var(--ink)}
</style>
</head>
<body>
<div class="stage">
  <main class="cover">
    <p class="centered volume-line"><span class="volume-tag">“VOLUME” 1</span> – MAPPING HIDDEN CURRENTS<br>WITHIN SHARED ENDEAVOURS</p>

    <h1>
      <span class="centered title-red title-lanterns">LANTERNS</span>
      <span class="ruled title-along"><span class="rule"></span><span class="word">ALONG THE</span><span class="rule right"></span></span>
      <span class="centered title-red title-river">RIVER</span>
    </h1>

    <div class="concept-art" role="img" aria-label="Illustration: a pinned sticky note naming the favoured way of governing, beside a crossed-out alternative"></div>

    <p class="centered subtitle">WEAVING A QUIETER<br>COMMONS</p>
    <p class="centered authors">LUCIEN MORVAN<br>ADRIAN WHITCOMBE</p>
  </main>
</div>
</body>
</html>
```